Quorvex - Automated robotic Inspection with AI need new business cards

We need a new design of our business cards. The company is focused on automated quality control at high speed with unmatched results. We have a logo but need a more forward leaning business card that shows that we are delivering cutting edge technology.

Contact Information for Business Card

Name
Position
Adress
Phone
Email
e.g.
Lena Holmqvist
Chief Financial Officer (CFO)

Quorvex Sweden AB
Bruksvägen 14, SE-175 43 JÄRFÄLLA, Sweden
Mobile: +46735 21 47 83 | Office: +46 8 61 94 27
www.quorvex-example.com

Font styles to use
Sans Serif

```html
<!DOCTYPE html>
<html lang="en">
<head>
<meta charset="utf-8">
<title>Quorvex Business Card</title>
<link rel="stylesheet" href="https://fonts.googleapis.com/css2?family=Arimo:wght@700&family=Fira+Sans:wght@400;500;600&display=swap">
<style>
  :root {
    --bg: #2e2c0a;
    --navy: #0c2c57;
    --brand-blue: #1d4f7c;
    --name-blue: #1f4470;
    --yellow: #fda705;
    --amber: #c46c0a;
    --ink: #111111;
    --paper: #ffffff;
    --back-dark: #02203a;
    --back-light: #1a5a8c;
  }
  * { box-sizing: border-box; margin: 0; padding: 0; }
  html, body {
    width: 1200px; height: 1200px; overflow: hidden;
    background: var(--bg);
  }
  .canvas {
    position: relative; width: 1200px; height: 1200px;
    display: flex; flex-direction: column; align-items: center; justify-content: center; gap: 60px;
  }
  .card {
    position: relative; width: 760px; height: 434px; overflow: hidden;
    box-shadow: 0 18px 40px rgba(0,0,0,0.45);
  }
  .card-front { background: var(--paper); }

  .edge-band {
    position: absolute; left: 0; top: 0; bottom: 0; width: 30px;
    background: var(--navy);
    border-right: 7px solid var(--yellow);
  }
  .foot-band {
    position: absolute; right: 0; bottom: 0; width: 200px; height: 30px;
    background: var(--navy);
    border-top: 5px solid var(--amber);
  }

  .wordmark {
    display: flex; align-items: center; gap: 14px;
    font-family: "Fira Sans", sans-serif; font-weight: 500; letter-spacing: 1px;
  }
  .wordmark-dot { border-radius: 50%; flex: none; }

  .card-front .wordmark {
    position: absolute; right: 75px; top: 44px;
    font-size: 54px; line-height: 1; color: var(--brand-blue);
  }
  .card-front .wordmark-dot { width: 30px; height: 30px; background: var(--brand-blue); }

  .person { position: absolute; right: 76px; top: 170px; text-align: right; }
  .person-name {
    font-family: "Arimo", sans-serif; font-weight: 700; font-size: 27px;
    color: var(--name-blue); letter-spacing: 0.3px; line-height: 1.1;
  }
  .person-title {
    font-family: "Fira Sans", sans-serif; font-weight: 400; font-size: 21px;
    color: var(--ink); margin-top: 6px;
  }

  .contact-list { position: absolute; left: 62px; top: 206px; list-style: none; }
  .contact-item {
    display: flex; align-items: flex-start; height: 35px;
    font-family: "Fira Sans", sans-serif; font-size: 20.5px; color: var(--ink); line-height: 31px;
  }
  .contact-item.primary { font-weight: 600; }
  .contact-item.address { height: auto; }
  .contact-icon {
    width: 31px; height: 31px; border-radius: 50%; background: var(--brand-blue);
    display: flex; align-items: center; justify-content: center; flex: none; margin-right: 14px;
  }
  .contact-icon svg { width: 17px; height: 17px; }
  .contact-text .sep { margin-right: 5px; }
  .address-line2 { display: block; padding-left: 11px; line-height: 30px; }

  .card-back {
    background: linear-gradient(30deg, var(--back-dark) 0%, #0a3358 45%, var(--back-light) 100%);
    display: flex; align-items: center; justify-content: center;
  }
  .card-back .wordmark { font-size: 76px; line-height: 1; color: var(--paper); }
  .card-back .wordmark-dot { width: 40px; height: 40px; background: var(--paper); }
</style>
</head>
<body>
<main class="canvas">

  <section class="card card-front" aria-label="Business card front">
    <div class="edge-band" aria-hidden="true"></div>
    <div class="foot-band" aria-hidden="true"></div>

    <div class="wordmark"><span class="wordmark-dot"></span><span>QUORVEX</span></div>

    <div class="person">
      <h1 class="person-name">LENA HOLMQVIST</h1>
      <p class="person-title">Chief Financial Officer</p>
    </div>

    <ul class="contact-list">
      <li class="contact-item primary">
        <span class="contact-icon"><svg viewBox="0 0 24 24"><path fill="#fff" d="M6.6 10.8a15.2 15.2 0 0 0 6.6 6.6l2.2-2.2c.3-.3.7-.4 1-.2 1.1.4 2.3.6 3.6.6.6 0 1 .4 1 1V20c0 .6-.4 1-1 1A17 17 0 0 1 3 4c0-.6.4-1 1-1h3.5c.6 0 1 .4 1 1 0 1.3.2 2.5.6 3.6.1.3 0 .7-.2 1z"/></svg></span>
        <span class="contact-text"><span class="sep">:</span>+46735 21 47 83</span>
      </li>
      <li class="contact-item">
        <span class="contact-icon"><svg viewBox="0 0 24 24"><path fill="#fff" d="M3 8c0-2 4-3.5 9-3.5S21 6 21 8v1.5h-4V8H7v1.5H3z"/><path fill="#fff" d="M7 11h10l2 9H5z"/><g fill="#1d4f7c"><rect x="9" y="13" width="1.6" height="1.4"/><rect x="11.2" y="13" width="1.6" height="1.4"/><rect x="13.4" y="13" width="1.6" height="1.4"/><rect x="9" y="15.4" width="1.6" height="1.4"/><rect x="11.2" y="15.4" width="1.6" height="1.4"/><rect x="13.4" y="15.4" width="1.6" height="1.4"/></g></svg></span>
        <span class="contact-text"><span class="sep">:</span>+46 8 61 94 27</span>
      </li>
      <li class="contact-item">
        <span class="contact-icon"><svg viewBox="0 0 24 24"><rect x="3" y="6" width="18" height="12" fill="none" stroke="#fff" stroke-width="1.6"/><path d="M3 6l9 7 9-7M3 18l7-6M21 18l-7-6" fill="none" stroke="#fff" stroke-width="1.4"/></svg></span>
        <span class="contact-text"><span class="sep">:</span>info@quorvex-example.com</span>
      </li>
      <li class="contact-item">
        <span class="contact-icon"><svg viewBox="0 0 24 24" fill="none" stroke="#fff" stroke-width="1.4"><circle cx="12" cy="12" r="9"/><ellipse cx="12" cy="12" rx="4" ry="9"/><path d="M3 12h18M4.5 7.5h15M4.5 16.5h15M12 3v18"/></svg></span>
        <span class="contact-text"><span class="sep">:</span>www.quorvex-example.com</span>
      </li>
      <li class="contact-item address">
        <span class="contact-icon"><svg viewBox="0 0 24 24"><path fill="#fff" d="M12 2a7 7 0 0 0-7 7c0 5 7 13 7 13s7-8 7-13a7 7 0 0 0-7-7z"/><path fill="#1d4f7c" d="M12 6l-3.5 3v4h7V9z"/></svg></span>
        <span class="contact-text"><span class="sep">:</span>Quorvex Sweden AB Bruksvägen 14, SE-175 43<span class="address-line2">JÄRFÄLLA, Sweden</span></span>
      </li>
    </ul>
  </section>

  <section class="card card-back" aria-label="Business card back">
    <div class="wordmark"><span class="wordmark-dot"></span><span>QUORVEX</span></div>
  </section>

</main>
</body>
</html>
```